independent cleaner, reliable, custom, thorough, trustworthy

Not sure yet if I want single-sided or double sided, so I'm selecting double-sided just in case, but single-sided designs are okay.

Really looking to find the happy medium between personal and professional in a business card design. I end up building comfortable relationships with the people I work for.

Most of my business is through referrals, but I want some business cards to hand out to people who ask for one (and maybe put them on community bulletin boards).

My target market is homeowners and business owners who are looking for a reliable cleaner and are willing to pay a bit more to have excellent quality and someone they trust.

Theme: I have a personal-professional feel since I'm solo, so the theme should reflect that. Trustworthy, personal, simple. I clean up messes.

Hopefully this is enough info, let me know if you have any questions though of course!

Target Market(s)

Homeowners businessowners who are looking for a reliable cleaner, excellent quality trustworthy.

Industry/Entity Type

Cleaning Service

Contact Information for Business Card

Please include this text:
• Delphine Warrow
• independent cleaner
• reliable, custom, thorough
• 604-317-2269
• mtb.warrow@postmail.example

Font styles to use
Serif
Sans Serif

Colors
ffffff
00a990
0492cd
33a6d7
0355a3
3276b5
919191

Requirements
Must have
• Really looking to find the happy medium between personal and professional in a business card design.
• Background: at least 50% white on the side with the most text (coloured accents or shapes are okay)
• I lean more towards simple and clean, solid colours, maybe a gentle gradient
Nice to have
• Not sure yet if I want single-sided or double sided, so I'm selecting double-sided just in case, but single-sided designs are okay.
• Colours: preferably blues and teals for the font and other objects (if any). Open to designer's choice though. I've toyed around with orangey-yellow, but it doesn't feel right and I keep going back to blues/teals
• Also I uploaded a sketch of my signature and initials so you can get a feel for my personality. I'm not expecting this to be included in the design, it's just there.
Should not have
• I don't like a lot of busy-ness or textures
• Also I don't have a logo (not sure where else to specify this)

```html
<!DOCTYPE html>
<html lang="en">
<head>
<meta charset="utf-8">
<title>Delphine Warrow – Business Card</title>
<link rel="stylesheet" href="https://fonts.googleapis.com/css2?family=Nunito+Sans:wght@200;300&display=swap">
<style>
  :root {
    --backdrop: #e2e2e2;
    --card: #ffffff;
    --name: #858585;
    --teal: #00a990;
    --sky: #33a6d7;
    --grey: #919191;
    --rule: #c4c4c4;
  }
  html, body {
    margin: 0;
    padding: 0;
    width: 1200px;
    height: 1200px;
    overflow: hidden;
    background: var(--backdrop);
    font-family: "Nunito Sans", sans-serif;
  }
  .business-card {
    position: absolute;
    left: 100px;
    top: 330px;
    width: 1000px;
    height: 540px;
    background: var(--card);
    text-align: center;
  }
  .identity {
    position: absolute;
    top: 128px;
    left: 0;
    right: 0;
  }
  .identity__name {
    margin: 0;
    font-weight: 200;
    font-size: 82px;
    line-height: 1;
    letter-spacing: 2px;
    color: var(--name);
  }
  .identity__role {
    margin: 16px 0 0;
    font-weight: 300;
    font-size: 48px;
    line-height: 1;
    color: var(--teal);
  }
  .identity__values {
    margin: 24px 0 0;
    font-weight: 300;
    font-size: 27px;
    line-height: 1;
    letter-spacing: 1px;
    color: var(--grey);
  }
  .divider {
    position: absolute;
    top: 396px;
    left: 0;
    width: 100%;
    height: 2px;
    background: var(--rule);
  }
  .contact {
    position: absolute;
    top: 426px;
    left: 0;
    right: 0;
    display: flex;
    justify-content: center;
    gap: 34px;
    font-weight: 300;
    font-size: 29px;
    color: var(--grey);
    letter-spacing: 0.5px;
  }
  .contact__item {
    display: flex;
    align-items: center;
    gap: 12px;
  }
  .contact__icon {
    stroke: var(--sky);
    fill: none;
    stroke-width: 1.6;
  }
</style>
</head>
<body>
  <main class="business-card">
    <section class="identity">
      <h1 class="identity__name">Delphine Warrow</h1>
      <p class="identity__role">independent cleaner</p>
      <p class="identity__values">reliable, custom, thorough</p>
    </section>
    <div class="divider"></div>
    <section class="contact">
      <span class="contact__item">
        <svg class="contact__icon" width="20" height="30" viewBox="0 0 20 30" aria-hidden="true">
          <rect x="2" y="1.5" width="16" height="27" rx="2"/>
          <line x1="2" y1="5.5" x2="18" y2="5.5"/>
          <line x1="2" y1="24" x2="18" y2="24"/>
        </svg>
        604-317-2269
      </span>
      <span class="contact__item">
        <svg class="contact__icon" width="30" height="20" viewBox="0 0 30 20" aria-hidden="true">
          <rect x="1.5" y="2" width="27" height="16"/>
          <polyline points="1.5,2 15,12 28.5,2"/>
          <line x1="1.5" y1="18" x2="11" y2="9.5"/>
          <line x1="28.5" y1="18" x2="19" y2="9.5"/>
        </svg>
        mtb.warrow@postmail.example
      </span>
    </section>
  </main>
</body>
</html>
```